R & T Summit Construction Business Card ideas

We want a business card to represents our company in a way that looks professional but is also a business card that is unique!

Industry/Entity Type

Construction Company

Contact Information for Business Card

open to all design ideas, just want to be able to see different options to choose from in either color or grayscale.

Requirements
Must have
• Our names and phone numbers
• Nolan Pritchett 512-804-2271
• Curtis Hale 512-693-1804
• Business logo

```html
<!DOCTYPE html>
<html lang="en">
<head>
<meta charset="utf-8">
<title>R &amp; T Summit Construction — Business Card</title>
<link href="https://fonts.googleapis.com/css2?family=Cinzel:wght@400;600&family=Open+Sans:wght@300&display=swap" rel="stylesheet">
<style>
  :root {
    --backdrop: #e9e6e1;
    --card: #f4f4f3;
    --card-edge: #dcdcdc;
    --panel: #0e0e0e;
    --panel-text: #f5f5f5;
    --ink: #2a2a2a;
    --ink-soft: #6a6a6a;
  }
  * { box-sizing: border-box; margin: 0; padding: 0; }
  html, body {
    width: 1200px; height: 1022px; overflow: hidden;
    background: var(--backdrop);
  }
  .stage {
    width: 1200px; height: 1022px;
    display: flex; align-items: center; justify-content: center;
  }
  .card {
    position: relative;
    width: 980px; height: 560px;
    background: linear-gradient(135deg, #ffffff 0%, var(--card) 60%, #eaeaea 100%);
    border-radius: 22px;
    box-shadow: 0 2px 0 var(--card-edge), 0 24px 50px rgba(0,0,0,.18);
  }
  .brand-panel {
    position: absolute;
    top: 52px; right: 70px;
    width: 560px; height: 300px;
    background: var(--panel);
    border-radius: 22px;
    display: flex; align-items: center; justify-content: center;
  }
  .brand-name {
    font-family: "Cinzel", serif;
    font-weight: 600;
    font-size: 40px;
    letter-spacing: 1px;
    color: var(--panel-text);
    text-align: center;
    line-height: 1.2;
  }
  .contacts {
    position: absolute;
    left: 70px; bottom: 58px;
    display: grid; gap: 4px;
  }
  .person {
    font-family: "Cinzel", serif;
    font-weight: 600;
    font-size: 26px;
    letter-spacing: 1.5px;
    color: var(--ink);
  }
  .phone {
    display: flex; align-items: center; gap: 10px;
    font-family: "Open Sans", sans-serif;
    font-weight: 300;
    font-size: 24px;
    color: var(--ink-soft);
    margin-bottom: 6px;
  }
  .phone svg { width: 16px; height: 16px; fill: var(--ink-soft); }
</style>
</head>
<body>
<main class="stage">
  <article class="card">
    <div class="brand-panel">
      <p class="brand-name">R &amp; T Summit<br>Construction</p>
    </div>
    <section class="contacts">
      <p class="person">Nolan Pritchett</p>
      <p class="phone">
        <svg viewBox="0 0 24 24" aria-hidden="true"><path d="M6.6 10.8a15.1 15.1 0 0 0 6.6 6.6l2.2-2.2a1 1 0 0 1 1-.25 11.4 11.4 0 0 0 3.6.6 1 1 0 0 1 1 1V20a1 1 0 0 1-1 1A17 17 0 0 1 3 4a1 1 0 0 1 1-1h3.5a1 1 0 0 1 1 1c0 1.25.2 2.45.6 3.6a1 1 0 0 1-.25 1z"/></svg>
        512-804-2271
      </p>
      <p class="person">Curtis Hale</p>
      <p class="phone">
        <svg viewBox="0 0 24 24" aria-hidden="true"><path d="M6.6 10.8a15.1 15.1 0 0 0 6.6 6.6l2.2-2.2a1 1 0 0 1 1-.25 11.4 11.4 0 0 0 3.6.6 1 1 0 0 1 1 1V20a1 1 0 0 1-1 1A17 17 0 0 1 3 4a1 1 0 0 1 1-1h3.5a1 1 0 0 1 1 1c0 1.25.2 2.45.6 3.6a1 1 0 0 1-.25 1z"/></svg>
        512-693-1804
      </p>
    </section>
  </article>
</main>
</body>
</html>
```